Stationery design bilingual preschool
Meadowlark preschool
Stationery design bilingual preschool - Childcare
Creative Brief
Bright & Fun-filled
Marita Sundqvist
Preschool director
Lövhagsvägen 9 128 31 Skarpnäck Sweden
angsfagelforskolan@postlada.se
www.angsfagelforskolan.com
Back of the business card suppose to have the same information as the front side but on Swedish.
(Subtitle) Ängsfågel Förskola AB ( name) Marita Sundqvist (title) Förskolechef (address) Lövhagsvägen 9 128 31 Skarpnäck (phone) Tel. 08 731 94 62 (cell) Mob. 073 862 40 15 (email) angsfagelforskolan@postlada.com (web side) www.angsfagelforskolan. com
butterfly2004 butterfly2004
Dear designers, I'd like to see design drafts ideas for the following products: 1. Business card 2. Letterhead 3. Envelope 4. Folder 5. CD and CD cover 6. Email signature 7. Presentation 8.Thank you card 8. Stamp 9. T-shirt, Hoody, Winter jacket/ Rain jacket, Cap, Scarf 10. Pen 11. Meadowlark character toy Thank you, PH

```html
<!DOCTYPE html>
<html lang="sv">
<head>
<meta charset="utf-8">
<title>Meadowlark Preschool – Business Card</title>
<link href="https://fonts.googleapis.com/css2?family=Open+Sans:wght@400;600;700;800&display=swap" rel="stylesheet">
<style>
  :root{
    --stage:#e9ebe8;
    --green:#5aa51c;
    --green-dark:#2f7d12;
    --green-light:#8ed13a;
    --orange:#f28c1c;
    --ink:#5b5f5c;
    --card:#ffffff;
  }
  *{box-sizing:border-box;margin:0;padding:0}
  html,body{width:1200px;height:869px;overflow:hidden}
  body{
    background:var(--stage);
    font-family:"Open Sans",Arial,sans-serif;
    display:flex;align-items:center;justify-content:center;gap:60px;
  }
  .card{
    width:540px;height:308px;border-radius:4px;position:relative;overflow:hidden;
    box-shadow:0 10px 30px rgba(0,0,0,.18);
  }
  /* back side */
  .card--back{
    background:radial-gradient(ellipse at 55% 45%,var(--green-light) 0%,var(--green) 45%,var(--green-dark) 100%);
    display:flex;align-items:center;justify-content:center;gap:14px;
  }
  .card--back .brand-dot{width:26px;height:26px;border-radius:50%;background:var(--orange)}
  .card--back .brand-name{font-weight:800;font-size:38px;color:#fff;line-height:1}
  /* front side */
  .card--front{background:var(--card);padding:38px 36px}
  .person-name{font-weight:700;font-size:21px;color:var(--green)}
  .person-title{font-weight:600;font-size:12.5px;color:var(--orange);margin-top:4px}
  .address{font-size:11.5px;color:var(--ink);margin-top:10px;line-height:1.45}
  .contacts{list-style:none;margin-top:22px}
  .contacts li{display:flex;align-items:center;gap:9px;font-size:11.5px;color:var(--ink);height:19px}
  .contacts svg{width:13px;height:13px;flex:none}
  .brand{position:absolute;right:34px;top:118px;text-align:left}
  .brand-row{display:flex;align-items:center;gap:10px}
  .brand-row .brand-dot{width:20px;height:20px;border-radius:50%;background:var(--orange)}
  .brand-row .brand-name{font-weight:800;font-size:25px;color:var(--green);line-height:1.05}
  .brand-sub{font-weight:700;font-size:19px;color:var(--green);margin-top:22px;text-align:center}
</style>
</head>
<body>
  <section class="card card--back" aria-label="Card back">
    <span class="brand-dot"></span>
    <span class="brand-name">Meadowlark Preschool</span>
  </section>

  <section class="card card--front" aria-label="Card front">
    <h1 class="person-name">Marita Sundqvist</h1>
    <p class="person-title">Preschool director | Förskolechef</p>
    <p class="address">Lövhagsvägen 9<br>128 31 Skarpnäck, Sweden</p>
    <ul class="contacts">
      <li><svg viewBox="0 0 16 16"><circle cx="8" cy="8" r="8" fill="#5aa51c"/><path d="M5 4.5l1.6-.4 1 2-1 .8a5 5 0 0 0 2.5 2.5l.8-1 2 1-.4 1.6c-3.6.2-6.7-2.9-6.5-6.5z" fill="#fff"/></svg>46 8 731 94 62</li>
      <li><svg viewBox="0 0 16 16"><circle cx="8" cy="8" r="8" fill="#5aa51c"/><rect x="5.5" y="3.5" width="5" height="9" rx="1" fill="#fff"/><rect x="6.5" y="5" width="3" height="5" fill="#5aa51c"/></svg>46 73 862 40 15</li>
      <li><svg viewBox="0 0 16 16"><circle cx="8" cy="8" r="8" fill="#5aa51c"/><rect x="4" y="5" width="8" height="6" rx=".6" fill="#fff"/><path d="M4 5.3l4 3 4-3" stroke="#5aa51c" stroke-width="1" fill="none"/></svg>angsfagelforskolan@postlada.se</li>
      <li><svg viewBox="0 0 16 16"><circle cx="8" cy="8" r="8" fill="#5aa51c"/><circle cx="8" cy="8" r="4" stroke="#fff" stroke-width="1" fill="none"/><path d="M4 8h8M8 4c-2 2.4-2 5.6 0 8M8 4c2 2.4 2 5.6 0 8" stroke="#fff" stroke-width=".8" fill="none"/></svg>www.angsfagelforskolan.com</li>
    </ul>
    <div class="brand">
      <div class="brand-row">
        <span class="brand-name">Meadowlark<br>Preschool</span>
        <span class="brand-dot"></span>
      </div>
      <p class="brand-sub">Ängsfågel Förskola</p>
    </div>
  </section>
</body>
</html>
```